Postcard Flyer For Plumbing Company

We are a p[professional plumbing company in NSW that carry out plumbing, electrical and hot water system work.
i want to send a postcard size flyer 105mm x 148mm to our clients to offer $xx off their next job they book with us.
The front of the flyer needs to say.... Feel The Love WIth $35 Off your Next Job. It needs to include a section where their name and postal address can go (74mm W x 24mm H) on the left hand side of the bottom of the flyer - refer attached example.
The other side of the flyer needs to have a section for text, the offer ($35 or $xx what they get off their next job) and also can use the tag line... Call 1 Number for The Best In 3 Trades - Plumbing, Hot Water & Electrical.
Plumbing, hot water and electrical pictures/icons can be used.
I want the flyer to stand out, use the corporate colours and be modern whilst letting them know that they can use this voucher on their next job.
Refer attachments.

Target Market(s)

Homeowners and our existing clients

Industry/Entity Type

Plumbing

Font styles to use
Serif

Colors
0255a3
ec1f27
ffffff
d3d3d3

Requirements
Must have
• Corporate colours and logos
• Red Colour:
• C=0
• M=100
• Y=100
• K=0
• Blue Colour
• C= 100
• M=66
• Y=0
• K=2
• Grey Colour
• C= 26
• M=21
• Y=19
• K=0
Nice to have
• predominately white background
Should not have
• Black background and lots of black.

```html
<!DOCTYPE html>
<html lang="en">
<head>
<meta charset="utf-8">
<title>Hartwell Contracting – Postcard Flyer</title>
<link rel="stylesheet" href="https://fonts.googleapis.com/css2?family=Bebas+Neue&family=Lato:wght@300;400;700;900&display=swap">
<style>
  :root {
    --blue: #0255a3;
    --blue-dark: #1c3f86;
    --red: #ec1f27;
    --white: #ffffff;
    --grey: #d3d3d3;
    --grey-light: #e6e6e8;
    --ink: #3d3d3d;
    --page: #f2f2f2;
  }
  * { box-sizing: border-box; margin: 0; padding: 0; }
  html, body { width: 1200px; height: 1200px; overflow: hidden; background: var(--page); }
  .canvas { position: relative; width: 1200px; height: 1200px; }
  .postcard {
    position: absolute; left: 260px; width: 795px; height: 565px;
    transform: scale(0.856); transform-origin: top left;
    background: var(--white); overflow: hidden;
    box-shadow: 0 4px 14px rgba(0,0,0,0.18);
    font-family: "Lato", sans-serif;
  }
  .postcard--front { top: 87px; }
  .postcard--back { top: 630px; }
  .postcard svg.shapes { position: absolute; inset: 0; width: 100%; height: 100%; }
  .postcard .abs { position: absolute; }

  /* Brand badge */
  .brand-badge {
    left: 100px; top: 17px; width: 170px; height: 170px; border-radius: 50%;
    background: var(--white); border: 4px solid var(--blue);
    display: flex; flex-direction: column; align-items: center; justify-content: center; text-align: center;
  }
  .brand-name { font-family: "Lato", sans-serif; font-weight: 900; color: var(--blue); line-height: 1.05; }
  .brand-badge .brand-name { font-size: 21px; }
  .brand-tagline { font-family: "Lato", sans-serif; font-weight: 700; color: #222; }
  .brand-badge .brand-tagline { font-size: 9px; margin-top: 8px; }

  .front-url {
    right: 43px; top: 40px; color: var(--white);
    font-family: "Bebas Neue", sans-serif; font-size: 30px; letter-spacing: 0.3px;
  }
  .offer { left: 43px; top: 200px; }
  .offer-lead { font-family: "Lato", sans-serif; font-weight: 700; font-size: 31px; color: var(--ink); letter-spacing: 0.3px; }
  .offer-amount { font-family: "Bebas Neue", sans-serif; font-size: 124px; line-height: 0.9; color: var(--red); margin-top: 8px; }
  .offer-note { font-family: "Bebas Neue", sans-serif; font-size: 66px; line-height: 0.95; color: var(--blue); margin-top: 6px; }

  .call-box { left: 470px; top: 455px; width: 325px; text-align: center; color: var(--white); }
  .call-label { font-weight: 300; font-size: 31px; }
  .call-number { font-weight: 700; font-size: 44px; line-height: 1.05; letter-spacing: 0.5px; }

  /* Back */
  .tagline { left: 537px; top: 74px; font-family: "Bebas Neue", sans-serif; color: var(--blue); }
  .tagline-line { font-size: 46px; line-height: 1; }
  .tagline-accent { font-size: 70px; line-height: 1; color: var(--red); }

  .back-brand { left: 520px; top: 368px; width: 260px; text-align: center; }
  .back-brand .brand-name { font-size: 36px; }
  .back-brand .brand-tagline { font-size: 14px; margin-top: 12px; }

  .contact-list { left: 30px; top: 445px; list-style: none; color: var(--white); font-size: 17px; }
  .contact-list li { display: flex; align-items: center; gap: 12px; height: 32px; }
  .contact-list svg { width: 18px; height: 18px; flex: none; }

  .voucher-badge {
    left: 318px; top: 373px; width: 178px; height: 178px; border-radius: 50%;
    background: var(--white); border: 4px solid var(--blue);
    display: flex; flex-direction: column; align-items: center; justify-content: center; text-align: center;
    box-shadow: 0 2px 6px rgba(0,0,0,0.2);
  }
  .voucher-amount { font-family: "Bebas Neue", sans-serif; font-size: 64px; line-height: 0.9; color: var(--red); }
  .voucher-note { font-family: "Bebas Neue", sans-serif; font-size: 19px; line-height: 1.25; color: var(--blue); margin-top: 4px; }
</style>
</head>
<body>
<main class="canvas">

  <!-- Front -->
  <section class="postcard postcard--front">
    <svg class="shapes" viewBox="0 0 795 565" preserveAspectRatio="none">
      <defs>
        <linearGradient id="electricianTone" x1="0" y1="0" x2="1" y2="1">
          <stop offset="0" stop-color="#d9dde3"/>
          <stop offset="0.5" stop-color="#3b63b4"/>
          <stop offset="1" stop-color="#1d3f8c"/>
        </linearGradient>
      </defs>
      <rect x="0" y="0" width="795" height="425" fill="var(--grey-light)"/>
      <polygon points="0,0 795,0 795,190 270,95 100,110 0,205" fill="var(--red)"/>
      <polygon role="img" aria-label="Photo of a smiling electrician in a blue hard hat testing a switchboard" points="370,140 795,200 795,423 355,423" fill="url(#electricianTone)"/>
      <polyline points="0,213 100,116 270,100 795,195" fill="none" stroke="var(--blue)" stroke-width="8"/>
      <rect x="0" y="423" width="795" height="14" fill="#c8161d"/>
      <rect x="0" y="437" width="795" height="128" fill="var(--white)"/>
      <line x1="43" y1="476" x2="432" y2="476" stroke="#555" stroke-width="1.2"/>
      <line x1="43" y1="520" x2="432" y2="520" stroke="#555" stroke-width="1.2"/>
      <polygon points="485,437 795,437 795,565 455,565" fill="var(--blue)"/>
    </svg>

    <div class="abs brand-badge">
      <div class="brand-name">HARTWELL<br>CONTRACTING</div>
      <div class="brand-tagline">Plumbing • Electrical • Hot Water</div>
    </div>
    <div class="abs front-url">WWW.HARTWELLCONTRACTING.COM.AU</div>

    <div class="abs offer">
      <div class="offer-lead">Feel The Love With</div>
      <div class="offer-amount">$35 OFF</div>
      <div class="offer-note">YOUR NEXT JOB</div>
    </div>

    <div class="abs call-box">
      <div class="call-label">Call us Today</div>
      <div class="call-number">0123456789</div>
    </div>
  </section>

  <!-- Back -->
  <section class="postcard postcard--back">
    <svg class="shapes" viewBox="0 0 795 565" preserveAspectRatio="none">
      <defs>
        <linearGradient id="plumberTone" x1="0" y1="0" x2="1" y2="1">
          <stop offset="0" stop-color="#eef1f4"/>
          <stop offset="0.45" stop-color="#8fa7d4"/>
          <stop offset="1" stop-color="#d8dde3"/>
        </linearGradient>
        <linearGradient id="panelTone" x1="0" y1="0" x2="0" y2="1">
          <stop offset="0" stop-color="#ececef"/>
          <stop offset="1" stop-color="#f7f7f8"/>
        </linearGradient>
      </defs>
      <rect x="0" y="0" width="795" height="565" fill="url(#panelTone)"/>
      <polygon points="522,0 795,0 795,262 462,310" fill="var(--grey-light)"/>
      <polygon role="img" aria-label="Photo of a plumber in a blue cap tightening a pipe fitting on a hot water system" points="0,0 522,0 448,370 470,565 0,565" fill="url(#plumberTone)"/>
      <polyline points="522,0 462,310 795,262" fill="none" stroke="var(--blue)" stroke-width="6"/>
      <line x1="462" y1="310" x2="448" y2="370" stroke="var(--blue)" stroke-width="6"/>
      <polygon points="0,393 318,460 478,565 0,565" fill="var(--blue)"/>
      <polyline points="0,393 318,460" fill="none" stroke="var(--red)" stroke-width="6"/>
      <line x1="470" y1="520" x2="490" y2="565" stroke="var(--red)" stroke-width="5"/>
    </svg>

    <div class="abs tagline">
      <div class="tagline-line">CALL 1 NUMBER</div>
      <div class="tagline-line">FOR THE BEST IN</div>
      <div class="tagline-accent">3 TRADES</div>
    </div>

    <div class="abs back-brand">
      <div class="brand-name">HARTWELL<br>CONTRACTING</div>
      <div class="brand-tagline">Plumbing • Electrical • Hot Water</div>
    </div>

    <ul class="abs contact-list">
      <li>
        <svg viewBox="0 0 18 18" fill="none" stroke="#fff" stroke-width="1.4"><rect x="1.5" y="2" width="15" height="14" rx="1.5"/><rect x="4" y="4.5" width="3" height="9"/><line x1="9.5" y1="6" x2="14" y2="6"/><line x1="9.5" y1="9" x2="14" y2="9"/><line x1="9.5" y1="12" x2="14" y2="12"/></svg>
        0123456789
      </li>
      <li>
        <svg viewBox="0 0 18 18" fill="none" stroke="#fff" stroke-width="1.4"><circle cx="9" cy="9" r="7.5"/><ellipse cx="9" cy="9" rx="3.3" ry="7.5"/><line x1="1.5" y1="9" x2="16.5" y2="9"/></svg>
        www.hartwellcontracting.com.au
      </li>
      <li>
        <svg viewBox="0 0 18 18" fill="none" stroke="#fff" stroke-width="1.4"><rect x="1.5" y="3.5" width="15" height="11" rx="1"/><polyline points="1.5,4 9,10 16.5,4"/></svg>
        info@hartwellcontracting.com.au
      </li>
    </ul>

    <div class="abs voucher-badge">
      <div class="voucher-amount">$100</div>
      <div class="voucher-note">WHAT THEY GET OFF<br>THEIR NEXT JOB</div>
    </div>
  </section>

</main>
</body>
</html>
```